J & M Holloway Carpet & Gutter Cleaning

We clean carpets and have an environmentally friendly gutter machine that cleans out the guttering leaving no mess
Phone 0427816350
or 0438261907

Industry/Entity Type

Business

```html
<!DOCTYPE html>
<html lang="en">
<head>
<meta charset="UTF-8">
<title>J &amp; M Holloway Carpet &amp; Gutter Cleaning – Business Card</title>
<link rel="stylesheet" href="https://fonts.googleapis.com/css2?family=Bebas+Neue&family=Arimo:wght@700&display=swap">
<style>
  :root {
    --backdrop: #c4c5c7;
    --card-white: #ffffff;
    --brand-blue: #3565b5;
    --brand-blue-light: #4878c6;
    --ink: #1d1d1f;
    --panel-dark: #1e1f21;
    --panel-dark-edge: #2a2b2e;
    --text-light: #ffffff;
  }
  * { margin: 0; padding: 0; box-sizing: border-box; }
  html, body {
    width: 1200px;
    height: 900px;
    overflow: hidden;
    background: var(--backdrop);
  }
  .stage {
    width: 1200px;
    height: 900px;
    display: flex;
    align-items: center;
    justify-content: center;
  }
  .business-card {
    width: 960px;
    height: 540px;
    background: var(--card-white);
    display: flex;
    flex-direction: column;
    box-shadow: 0 14px 30px rgba(0,0,0,0.18);
  }
  .card-header {
    height: 288px;
    display: flex;
    flex-direction: column;
    align-items: center;
    justify-content: flex-end;
    padding-bottom: 40px;
  }
  .business-name {
    font-family: "Bebas Neue", sans-serif;
    font-weight: 400;
    font-size: 140px;
    line-height: 0.85;
    letter-spacing: 6px;
    color: var(--brand-blue);
    white-space: nowrap;
  }
  .service-line {
    font-family: "Bebas Neue", sans-serif;
    font-weight: 400;
    font-size: 46px;
    line-height: 1;
    letter-spacing: 0.33em;
    margin-right: -0.33em;
    color: var(--ink);
    margin-top: 14px;
    white-space: nowrap;
  }
  .accent-band {
    height: 34px;
    background: linear-gradient(90deg, var(--brand-blue), var(--brand-blue-light) 50%, var(--brand-blue));
  }
  .contact-panel {
    flex: 1;
    background: radial-gradient(ellipse at 50% 40%, var(--panel-dark-edge), var(--panel-dark) 70%);
    display: flex;
    flex-direction: column;
    align-items: center;
    justify-content: center;
    gap: 18px;
    padding-bottom: 22px;
  }
  .phone-line {
    display: flex;
    align-items: center;
    gap: 14px;
    font-family: "Arimo", sans-serif;
    font-weight: 700;
    font-size: 42px;
    line-height: 1;
    color: var(--text-light);
    letter-spacing: 1px;
  }
  .phone-icon {
    width: 40px;
    height: 40px;
    fill: var(--brand-blue-light);
    flex-shrink: 0;
  }
</style>
</head>
<body>
  <main class="stage">
    <article class="business-card">
      <header class="card-header">
        <h1 class="business-name">J &amp; M HOLLOWAY</h1>
        <p class="service-line">CARPET &amp; GUTTER CLEANING</p>
      </header>
      <div class="accent-band"></div>
      <section class="contact-panel">
        <p class="phone-line">
          <svg class="phone-icon" viewBox="0 0 24 24" aria-hidden="true">
            <path d="M6.6 10.8c1.4 2.8 3.8 5.1 6.6 6.6l2.2-2.2c.3-.3.7-.4 1-.2 1.1.4 2.3.6 3.6.6.6 0 1 .4 1 1V20c0 .6-.4 1-1 1C10.6 21 3 13.4 3 4c0-.6.4-1 1-1h3.5c.6 0 1 .4 1 1 0 1.3.2 2.5.6 3.6.1.3 0 .7-.2 1l-2.3 2.2z"/>
          </svg>
          <span class="phone-number">042 781 6350</span>
        </p>
        <p class="phone-line">
          <svg class="phone-icon" viewBox="0 0 24 24" aria-hidden="true">
            <path d="M6.6 10.8c1.4 2.8 3.8 5.1 6.6 6.6l2.2-2.2c.3-.3.7-.4 1-.2 1.1.4 2.3.6 3.6.6.6 0 1 .4 1 1V20c0 .6-.4 1-1 1C10.6 21 3 13.4 3 4c0-.6.4-1 1-1h3.5c.6 0 1 .4 1 1 0 1.3.2 2.5.6 3.6.1.3 0 .7-.2 1l-2.3 2.2z"/>
          </svg>
          <span class="phone-number">043 826 1907</span>
        </p>
      </section>
    </article>
  </main>
</body>
</html>
```